flyer for roofing advertising

Need a modern, bold, luxurious advertisement flyer for our roofing company. located in buffalo, ny. Big house with a intense roof design asphalt shingles. slogan is "Reliability starts at the top". Colors varies but want it to be modern. we will be handing these out when we are working in the area. phone number is 716-555-0147 for the NO K.W estimate. also our services are roofing, roof repairs, gutters, attic ventilation. we offer a 15 year warranty with our platinum roof program. We are certified by dwellmatch, harlan trevisk, quarno. Also follow us on linkpage, wexora and frunt. website is ktw-roofing.com, linkpage is ktwroofing. pictures are on linkpage and our website if need more can be provided. also can include a review we have.

```html
<!DOCTYPE html>
<html lang="en">
<head>
<meta charset="utf-8">
<title>KTW Roofing Flyer</title>
<link href="https://fonts.googleapis.com/css2?family=Bebas+Neue&family=Montserrat:wght@400;500;600;700;800&display=swap" rel="stylesheet">
<style>
:root{
  --orange:#f39325;
  --charcoal:#5f5f5f;
  --ink:#2b2b2b;
  --white:#ffffff;
  --backdrop:#a9a9a9;
  --partner-red:#e3141f;
}
*{box-sizing:border-box;margin:0;padding:0}
html,body{width:1200px;height:846px;overflow:hidden;background:var(--backdrop)}
body{position:relative;font-family:"Montserrat",sans-serif}
.flyer{
  position:absolute;left:320px;top:27px;width:595px;height:842px;
  transform:scale(0.94);transform-origin:0 0;
  background:var(--white);overflow:hidden;
  box-shadow:0 8px 24px rgba(0,0,0,.3);
}
.abs{position:absolute}
.brand{left:26px;top:28px;width:160px}
.brand-name{display:flex;align-items:center;gap:8px;color:var(--orange);font-weight:800;font-size:30px;letter-spacing:2px;margin-left:26px}
.brand-name .mark{width:14px;height:14px;background:var(--orange)}
.brand-tag{color:var(--orange);font-size:8.5px;font-weight:600;letter-spacing:.3px;margin-top:8px}
.website{right:28px;top:42px;font-size:12px;color:var(--ink);font-weight:500}
.hero{left:0;top:0;width:595px;height:594px}
.headline{left:28px;top:390px;font-family:"Bebas Neue",sans-serif;font-weight:400;color:var(--white);line-height:.95}
.headline .l1{font-size:36px;display:block}
.headline .l2{font-size:52px;display:block;margin-top:2px}
.services{left:288px;top:384px;display:flex;gap:6px;list-style:none}
.service{width:64px;text-align:center;color:var(--white);font-size:10.5px;font-weight:500;line-height:1.15}
.service .badge{width:44px;height:44px;border-radius:50%;background:var(--white);margin:0 auto 8px;display:flex;align-items:center;justify-content:center;border:2px solid var(--charcoal)}
.gallery{left:27px;top:476px;display:flex;gap:5px}
.gallery .thumb{width:104px;height:104px;border:2px solid var(--white)}
.t1{background:linear-gradient(180deg,#8a9ab0,#4b4038 60%,#6b7a4e)}
.t2{background:linear-gradient(180deg,#c8ccd0,#8e8a80 55%,#5c6646)}
.t3{background:linear-gradient(180deg,#a7b1a8,#e9edf1 40%,#8a6c6e 85%)}
.t4{background:linear-gradient(180deg,#7c8a94,#e4e6e8 40%,#9a6a3e 80%)}
.t5{background:linear-gradient(180deg,#8ea4c4,#6a3e2a 55%,#d5d8dc)}
.warranty{left:0;top:594px;width:595px;height:58px}
.warranty-text{left:0;top:602px;width:595px;text-align:center;color:var(--white);font-weight:700;font-size:16.5px;line-height:1.45}
.partners{left:28px;top:672px;width:545px;display:flex;justify-content:space-between;align-items:center}
.partner{display:flex;align-items:center;gap:8px;font-weight:700;font-size:19px;color:var(--ink)}
.partner .box{width:22px;height:22px;background:var(--orange)}
.partner .box.red{background:var(--partner-red)}
.social{right:28px;top:744px;font-size:10px;font-weight:700;color:var(--ink);letter-spacing:.3px}
.footer{left:0;top:773px;width:595px;height:69px;background:var(--orange)}
.address{left:34px;top:802px;display:flex;align-items:center;gap:10px;color:var(--white);font-size:12px;font-weight:500}
.estimate{right:42px;top:783px;color:var(--white);text-align:right}
.estimate .label{font-size:16px;font-weight:700;color:var(--ink);margin-right:4px}
.estimate .phone{display:flex;align-items:center;gap:8px;font-size:29px;font-weight:800;line-height:1}
</style>
</head>
<body>
<main class="flyer">
  <svg class="abs hero" viewBox="0 0 595 594" aria-hidden="true">
    <defs>
      <linearGradient id="sky" x1="0" y1="0" x2="0" y2="1">
        <stop offset="0" stop-color="#7c7fa6"/>
        <stop offset=".35" stop-color="#c9a3a8"/>
        <stop offset=".55" stop-color="#6d7184"/>
        <stop offset=".8" stop-color="#8a8c90"/>
        <stop offset="1" stop-color="#5c6a4a"/>
      </linearGradient>
    </defs>
    <polygon points="0,90 292,110 300,70 595,95 595,400 0,400" fill="var(--charcoal)"/>
    <polygon points="0,97 290,117 300,78 595,100 595,340 300,335 290,385 0,365" fill="url(#sky)" role="img" aria-label="Two-storey suburban house with dark asphalt shingle roof at dusk"/>
    <polygon points="0,372 292,392 302,342 595,347 595,400 0,400" fill="var(--charcoal)"/>
    <polygon points="0,380 294,398 305,350 595,354 595,585 0,585" fill="var(--orange)"/>
  </svg>

  <div class="abs brand">
    <div class="brand-name"><span class="mark"></span>KTW</div>
    <div class="brand-tag">ROOFING-SIDING-STONE</div>
  </div>
  <div class="abs website">www.ktw-roofing.com</div>

  <h1 class="abs headline"><span class="l1">RELIABILITY STARTS</span><span class="l2">AT THE TOP</span></h1>

  <ul class="abs services">
    <li class="service"><div class="badge"><svg width="26" height="22" viewBox="0 0 26 22"><g fill="#333"><rect x="1" y="2" width="24" height="5"/><rect x="1" y="9" width="24" height="5"/><rect x="1" y="16" width="24" height="5"/></g><g stroke="#fff" stroke-width="1.5"><path d="M7 2v5M13 2v5M19 2v5M4 9v5M10 9v5M16 9v5M22 9v5M7 16v5M13 16v5M19 16v5"/></g></svg></div>ROOFING</li>
    <li class="service"><div class="badge"><svg width="26" height="16" viewBox="0 0 26 16"><path d="M2 14L13 3l11 11" fill="none" stroke="#333" stroke-width="2.5"/></svg></div>ROOF<br>REPAIRS</li>
    <li class="service"><div class="badge"><svg width="22" height="22" viewBox="0 0 22 22"><g fill="#333"><rect x="1" y="1" width="9" height="5"/><rect x="12" y="1" width="9" height="5"/><rect x="1" y="8.5" width="9" height="5"/><rect x="12" y="8.5" width="9" height="5"/><rect x="1" y="16" width="9" height="5"/><rect x="12" y="16" width="9" height="5"/></g></svg></div>GUTTERS</li>
    <li class="service"><div class="badge"><svg width="30" height="30" viewBox="0 0 30 30"><circle cx="15" cy="15" r="14" fill="#222"/><g fill="#fff"><ellipse cx="15" cy="8" rx="4" ry="6"/><ellipse cx="9" cy="19" rx="6" ry="4" transform="rotate(-30 9 19)"/><ellipse cx="21" cy="19" rx="6" ry="4" transform="rotate(30 21 19)"/></g><circle cx="15" cy="15" r="2.5" fill="#222"/></svg></div>ATTIC<br>VENTILATION</li>
  </ul>

  <div class="abs gallery">
    <div class="thumb t1" role="img" aria-label="Crew on ladders working on a two-storey home"></div>
    <div class="thumb t2" role="img" aria-label="Work truck parked outside a house in winter"></div>
    <div class="thumb t3" role="img" aria-label="Snow-covered roof with shingles being replaced"></div>
    <div class="thumb t4" role="img" aria-label="Roofer removing old roofing on a snowy day"></div>
    <div class="thumb t5" role="img" aria-label="Wood-sided house with ladder and trailer"></div>
  </div>

  <svg class="abs warranty" viewBox="0 0 595 58" aria-hidden="true">
    <polygon points="0,0 595,0 595,8 540,8 520,58 75,58 55,8 0,8" fill="var(--charcoal)"/>
  </svg>
  <p class="abs warranty-text">WE OFFER A 15 YEAR WARRANTY WITH OUR<br>PLATINUM ROOF PROGRAM</p>

  <div class="abs partners">
    <div class="partner"><span class="box"></span>dwellmatch</div>
    <div class="partner"><span class="box red"></span>harlan trevisk</div>
    <div class="partner"><span class="box red"></span>quarno</div>
  </div>

  <div class="abs social">frunt · linkpage · wexora</div>

  <div class="abs footer"></div>
  <div class="abs address">
    <svg width="14" height="20" viewBox="0 0 14 20"><path d="M7 0a7 7 0 0 0-7 7c0 5 7 13 7 13s7-8 7-13a7 7 0 0 0-7-7z" fill="var(--charcoal)"/><circle cx="7" cy="7" r="2.5" fill="var(--orange)"/></svg>
    2187 Marrow Ln, Lockport, NY14094
  </div>
  <div class="abs estimate">
    <div class="label">NO K.W ESTIMATE</div>
    <div class="phone"><svg width="22" height="30" viewBox="0 0 22 30"><path d="M6 1l5 7-4 3c2 5 4 8 8 10l3-3 4 6-5 4C8 28 1 17 1 5z" fill="var(--charcoal)"/></svg>716-555-0147</div>
  </div>
</main>
</body>
</html>
```